Corporate Design für Onlineshop zum Verkauf von asiatischen Reflexbögen
Ein tolles Design und hervorragende Zusammenarbeit! Alle unsere Sonderwünsche wurden einwandfrei umgesetzt. Ich kann Vrelmo aus vollstem Herzen empfehlen. Unser Gewinner!
Zielgruppe
Ich bin Einzelunternehmer (Marwend Bogensport Helmut Drabeck) und verkaufe in meinem Webshop Asiatische Reflexbögen, häufig auch als Reiterbögen bezeichnet, und alles was der traditionelle Bogenschütze so braucht (z.B. Pfeile, Köcher, Zubehör, etc...)
Aufgabenstellung
Ich suche ein einprägsames Design, das in verschiedenen Größen gut funktioniert und erkennbar ist (sowohl als kleines Logo als auch größer auf Messeständen oder Flyern).
Das Logo sollte am Besten sowohl farbig (z.B. Onlineshop, Visitenkarte, Briefkopf) als auch schwarz/weiß (z.B. als Gravur auf Leder oder Holz) funktionieren.
Wenn die Silouhette eines gespannten typischen Reiterbogens (tatarisch, mongolisch, skytisch oder chinesisch) im Logo drin wäre und ein stilisierter Fuchs, dann würde das den Namen villeicht ganz gut untermalen glaub ich.
Meine Hauptkunden sind Bogenschützen, die vornehmlich mit traditionellen Bögen schießen, sowohl auf dem Platz als auch in der Natur auf dem 3D-Parcours.
Der Name MarWend leitet sich von 'fux = Fuchs' und 'luoga = versteckter Wohnung' ab, heißt also in etwa 'Fuchsbau' so sind hier im Süddeutschen und Österreichischen einige Ortsteile bzw. Einöden benannt, z.B. Marwend oder Fuchslug in Aschau im Chiemgau.
Meinen Onlineshop baue ich gerade auf, da ist also noch nicht wirklich was zu sehen. Ich brauche daher ein Logo für Shop, Visitenkarte und Briefpapier und ein Design für Visitenkarte und ein Design für Briefpapier/Rechnungen.

```html
<!DOCTYPE html>
<html lang="de">
<head>
<meta charset="utf-8">
<title>MarWend Bogensport – Corporate Design</title>
<link rel="stylesheet" href="https://fonts.googleapis.com/css2?family=Open+Sans:ital,wght@0,400;0,600;0,700;0,800;1,700&family=Poppins:wght@400&display=swap">
<style>
  :root {
    --orange: #dd5f10;
    --brown: #3a1a0a;
    --cream: #f4eeea;
    --paper: #ffffff;
    --text: #2a1a12;
  }
  * { margin: 0; padding: 0; box-sizing: border-box; }
  html, body { width: 1200px; height: 2400px; overflow: hidden; }
  body {
    position: relative;
    background: var(--orange);
    font-family: "Open Sans", sans-serif;
    color: var(--text);
  }
  .shadow { box-shadow: 0 10px 28px rgba(60, 20, 0, 0.35); }

  /* Logo tile */
  .logo-tile {
    position: absolute; left: 353px; top: 147px; width: 496px; height: 496px;
    background: var(--cream); border-radius: 20px;
    display: flex; flex-direction: column; align-items: center; justify-content: center; gap: 28px;
  }
  .logo-dot { width: 150px; height: 150px; border-radius: 50%; background: var(--orange); }
  .brand-name { font-weight: 700; color: var(--brown); line-height: 1; }
  .logo-tile .brand-name { font-size: 64px; }

  /* Business card back */
  .card-back {
    position: absolute; left: 468px; top: 824px; width: 501px; height: 288px;
    background: var(--cream); overflow: hidden;
  }
  .card-back .brand-name { position: absolute; left: 31px; top: 36px; font-size: 52px; color: var(--orange); }
  .card-back .card-dot {
    position: absolute; left: 320px; top: 100px; width: 200px; height: 200px;
    border-radius: 50%; background: var(--orange);
  }

  /* Business card front */
  .card-front {
    position: absolute; left: 231px; top: 956px; width: 502px; height: 286px;
    background: var(--cream); overflow: hidden;
  }
  .card-front .panel { position: absolute; left: 0; top: 0; width: 502px; height: 286px; }
  .card-front .mini-brand { position: absolute; left: 36px; top: 70px; font-size: 20px; color: var(--orange); }
  .holder-name { position: absolute; left: 31px; top: 120px; font-size: 25px; font-weight: 600; color: var(--text); }
  .holder-rule { position: absolute; left: 31px; top: 166px; width: 44px; height: 2px; background: var(--orange); }
  .contact { position: absolute; font-size: 10px; line-height: 14px; color: var(--text); }
  .contact .company { font-size: 13px; font-weight: 700; line-height: 18px; }
  .contact .company .mark { color: var(--orange); }
  .contact .row { display: flex; }
  .contact .key { width: 20px; }
  .card-front .contact { left: 31px; top: 172px; }

  .range-list { position: absolute; left: 0; top: 0; width: 502px; height: 286px; list-style: none; }
  .range-list li {
    position: absolute; right: 28px; height: 25px;
    background: linear-gradient(90deg, var(--orange) 0%, #a8430f 50%, var(--brown) 100%);
    color: #fff; font-style: italic; font-weight: 700; font-size: 17px;
    display: flex; align-items: center; justify-content: flex-end;
    padding-right: 30px; line-height: 20px; text-align: right; white-space: nowrap;
  }
  .range-list li::after {
    content: ""; position: absolute; right: -3px; top: 50%; width: 11px; height: 11px; margin-top: -5.5px;
    border: 2px solid #d9d2cc; border-radius: 50%; background: var(--brown);
  }
  .range-list .item-reflex   { left: 328px; top: 29px; height: 46px; }
  .range-list .item-reiter   { left: 315px; top: 86px; }
  .range-list .item-lang     { left: 302px; top: 122px; }
  .range-list .item-pfeile   { left: 288px; top: 159px; }
  .range-list .item-ziele    { left: 275px; top: 197px; }
  .range-list .item-zubehoer { left: 261px; top: 234px; }

  /* Letterhead */
  .letterhead {
    position: absolute; left: 254px; top: 1423px; width: 692px; height: 884px;
    background: var(--paper);
  }
  .letterhead .lh-brand { position: absolute; left: 67px; top: 70px; font-size: 26px; color: var(--orange); }
  .letterhead .lh-brand-rule { position: absolute; left: 67px; top: 141px; width: 39px; height: 4px; background: var(--orange); }
  .letterhead .contact { left: 482px; top: 32px; font-size: 12px; line-height: 16px; }
  .letterhead .contact .company { font-size: 16px; line-height: 20px; }
  .letterhead .contact .key { width: 24px; }
  .double-rule {
    position: absolute; left: 67px; top: 244px; width: 557px; height: 6px;
    border-top: 2px solid var(--brown); border-bottom: 1px solid var(--brown);
  }
  .headline { position: absolute; left: 67px; top: 274px; font-size: 22px; font-weight: 800; color: var(--brown); }
  .body-copy { position: absolute; left: 67px; top: 330px; width: 557px; font-size: 8.6px; line-height: 12.7px; text-align: justify; color: var(--text); }
  .body-copy p + p { margin-top: 12.7px; }
  .signoff { position: absolute; left: 484px; top: 712px; font-family: "Poppins", sans-serif; font-size: 10px; color: var(--text); }
  .signoff .sig-line { display: block; width: 120px; height: 30px; margin: 2px 0 2px -34px; }
  .bank { position: absolute; left: 67px; top: 772px; padding-left: 22px; border-left: 8px solid var(--orange); }
  .bank h3 { font-size: 19px; font-weight: 600; color: var(--brown); line-height: 28px; }
  .bank p { font-size: 19px; letter-spacing: 3px; color: var(--text); line-height: 30px; }
</style>
</head>
<body>

  <section class="logo-tile shadow" aria-label="Logo">
    <div class="logo-dot"></div>
    <div class="brand-name">MarWend</div>
  </section>

  <section class="card-back shadow" aria-label="Visitenkarte Rückseite">
    <div class="brand-name">MarWend</div>
    <div class="card-dot"></div>
  </section>

  <section class="card-front shadow" aria-label="Visitenkarte Vorderseite">
    <svg class="panel" viewBox="0 0 502 286" aria-hidden="true">
      <polygon points="300,0 502,0 502,286 224,286 256,174 250,174" fill="#dd5f10"/>
      <polygon points="318,0 502,0 502,286 246,286 278,174 272,174 300,52 306,52" fill="#3a1a0a"/>
    </svg>
    <div class="brand-name mini-brand">MarWend</div>
    <div class="holder-name">Helmut Drabeck</div>
    <div class="holder-rule"></div>
    <div class="contact">
      <div class="company"><span class="mark">MarWend</span> Bogensport</div>
      <div class="row"><span class="key">A :</span><span>Lindenweg 16<br>83371 Talbruck</span></div>
      <div class="row"><span class="key">T :</span><span>0049 170 5550142</span></div>
      <div class="row"><span class="key">E :</span><span>helmut@marwend.de</span></div>
      <div class="row"><span class="key">W :</span><span>www.MarWend.de</span></div>
    </div>
    <ul class="range-list">
      <li class="item-reflex">Asiatische<br>Reflexbögen</li>
      <li class="item-reiter">Reiterbögen</li>
      <li class="item-lang">Langbögen</li>
      <li class="item-pfeile">Pfeile</li>
      <li class="item-ziele">3-D Ziele</li>
      <li class="item-zubehoer">Zubehör</li>
    </ul>
  </section>

  <section class="letterhead" aria-label="Briefpapier">
    <div class="brand-name lh-brand">MarWend</div>
    <div class="lh-brand-rule"></div>
    <div class="contact">
      <div class="company"><span class="mark">MarWend</span> Bogensport</div>
      <div class="row"><span class="key">A :</span><span>Lindenweg 16<br>83371 Talbruck</span></div>
      <div class="row"><span class="key">T :</span><span>0049 170 5550142</span></div>
      <div class="row"><span class="key">E :</span><span>helmut@marwend.de</span></div>
      <div class="row"><span class="key">W :</span><span>www.MarWend.de</span></div>
    </div>
    <div class="double-rule"></div>
    <h2 class="headline">HEADLINE</h2>
    <div class="body-copy">
      <p>Lorem ipsum dolor sit amet, consectetur adipiscing elit. Cras non lacus nisi. Vestibulum quis nisi vel neque volutpat ornare in sed purus. Aliquam vel feugiat dui. Nam elementum eros eget euismod congue. Etiam quis dictum diam. Vestibulum eget leo finibus, volutpat purus ut, tincidunt quam. Nunc a ipsum vel ante facilisis malesuada eu vitae magna. Etiam eu porta ex, non tristique nisl. Nam nec odio laoreet, vestibulum est sit amet, pulvinar enim. Curabitur nec sem tempor, luctus orci nec, iaculis enim. Integer venenatis quis tortor vel egestas. Vivamus ac nunc vel velit convallis posuere ac tincidunt nisl.</p>
      <p>Pellentesque in placerat felis. Aenean sed leo vel metus pellentesque elementum. Donec aliquam hendrerit dictum. Sed tincidunt quam sed auctor imperdiet. Vivamus mollis imperdiet nunc, at consectetur diam facilisis facilisis. Etiam dignissim, nulla nec feugiat gravida, ante nibh fermentum arcu, sed efficitur orci sapien id nisi. Donec id metus quis leo consectetur maximus non ac turpis.</p>
      <p>Mauris sed odio eget ex pretium interdum vel sed ex. Phasellus tristique risus nec turpis fringilla condimentum. Pellentesque eros odio, porttitor eu ultricies vitae, pulvinar id felis. Quisque a lobortis ipsum. Nam sem nulla, pellentesque at nisi vel, efficitur commodo ligula. In et ipsum dapibus, pellentesque sapien sed, vestibulum eros. In vulputate felis id est commodo, et faucibus eros molestie. Duis iaculis arcu turpis, at ornare nunc malesuada in. Sed aliquam, nulla sed laoreet viverra, nibh lacus fermentum nisl, id malesuada urna elit in orci. Maecenas diam purus, aliquam vitae enim et, fermentum accumsan erat. Nullam nisi urna, vulputate non nulla dictum, aliquam dignissim mi. Proin ac neque sed sapien lobortis blandit vel sit amet urna. Nulla venenatis pretium arcu, nec commodo purus fermentum vel. Nunc eu metus ultricies, maximus magna sit amet, sollicitudin nulla.</p>
      <p>Aliquam augue nisi, molestie in sollicitudin eget, iaculis id neque. Nunc sollicitudin iaculis varius. Fusce eu ipsum felis. Mauris non orci bibendum, ultrices nulla in, volutpat mauris. Vestibulum aliquam blandit lectus, quis laoreet diam rhoncus sed. Donec quis fringilla nunc. Vestibulum in sagittis eros. Nulla hendrerit justo non pharetra tristique. Praesent dictum, libero ac blandit scelerisque, nisl odio efficitur neque, non ullamcorper elit nunc non magna. Duis sit amet volutpat diam. Ut dictum tempus porta.</p>
    </div>
    <div class="signoff">
      <span>Your name</span>
      <svg class="sig-line" viewBox="0 0 120 30" aria-hidden="true">
        <path d="M4 24 C14 8, 22 6, 18 18 S 30 26, 40 14 S 58 10, 66 16 S 88 6, 100 12 S 112 4, 118 2" fill="none" stroke="#2a1a12" stroke-width="1"/>
      </svg>
      <span>Chairman</span>
    </div>
    <div class="bank">
      <h3>Bankverbindung</h3>
      <p>IBAN: DE00 1234</p>
    </div>
  </section>

</body>
</html>
```